Steady Harvest of Patrons Programme Graphic

Please refer to attached graphic.
I wish to redesign this graphic to represent a programme of work that we (Brinvo) deliver to our customers.
The design represents 9 steps ( 3 steps at each of 3 levels) and is all about implementing the 'Steady Harvest of Patrons'

I like the fact that the increasing business growth is evident when you are progressing through the stages, but the current graphic looks dated and the colours are not working.
I would also like to incorporate the SHP logo we have created.

Target Market(s)

IT Sector - businesses looking to grow

Industry/Entity Type

We are a digital marketing company

Requirements
Must have
• Clear, concise design
Should not have
• Design must not be complicated

```html
<!DOCTYPE html>
<html lang="en">
<head>
<meta charset="utf-8">
<title>Steady Harvest of Patrons – Programme Graphic</title>
<link rel="stylesheet" href="https://fonts.googleapis.com/css2?family=Exo:ital,wght@0,400;0,500;0,600;1,800&family=Barlow:wght@400&family=Saira+Condensed:wght@800&display=swap">
<style>
  :root {
    --bg-top: #fdfdfd;
    --bg-bottom: #edefef;
    --accent-blue: #4ab6ec;
    --brand-blue: #1a9ad6;
    --number-gold: #f7c600;
    --title-grey: #c4c4c4;
    --guide-grey: #9a9a9a;
    --face-text: #ffffff;
  }
  html, body {
    margin: 0;
    padding: 0;
    width: 1200px;
    height: 832px;
    overflow: hidden;
  }
  body {
    background: linear-gradient(160deg, var(--bg-top) 0%, var(--bg-bottom) 100%);
  }
  .programme-graphic {
    display: block;
    width: 1200px;
    height: 832px;
  }
  .axis-label {
    font-family: "Exo", sans-serif;
    font-weight: 500;
    font-size: 66px;
    fill: var(--accent-blue);
  }
  .guide-line {
    stroke: var(--guide-grey);
    stroke-width: 2;
    stroke-dasharray: 2 9;
    stroke-linecap: round;
  }
  .step-number {
    font-family: "Exo", sans-serif;
    font-style: italic;
    font-weight: 800;
    font-size: 170px;
    fill: none;
    stroke: var(--number-gold);
    stroke-width: 5;
  }
  .stage-name {
    font-family: "Saira Condensed", sans-serif;
    font-weight: 800;
    font-size: 64px;
    fill: var(--face-text);
    fill-opacity: 0.55;
    letter-spacing: 1px;
  }
  .step-label {
    font-family: "Exo", sans-serif;
    font-weight: 500;
    font-size: 31px;
    fill: var(--face-text);
    letter-spacing: 1px;
  }
  .programme-title {
    font-family: "Exo", sans-serif;
    font-weight: 600;
    font-size: 60px;
    fill: var(--title-grey);
  }
  .brand-name {
    font-family: "Exo", sans-serif;
    font-weight: 600;
    font-size: 78px;
    fill: var(--brand-blue);
  }
  .legend-text {
    font-family: "Barlow", sans-serif;
    font-weight: 400;
    font-size: 38px;
    fill: var(--accent-blue);
  }
  .legend-line {
    stroke: var(--accent-blue);
    stroke-width: 1.5;
    opacity: 0.7;
  }
  .legend-dot {
    fill: var(--accent-blue);
  }
</style>
</head>
<body>
<svg class="programme-graphic" viewBox="0 0 2302 1596" preserveAspectRatio="xMidYMid meet" xmlns="http://www.w3.org/2000/svg">
  <defs>
    <linearGradient id="face-left" x1="0" y1="0" x2="0" y2="1">
      <stop offset="0" stop-color="#6399bb"/>
      <stop offset="0.6" stop-color="#84b5c6"/>
      <stop offset="1" stop-color="#bfe0da"/>
    </linearGradient>
    <linearGradient id="face-right" x1="0" y1="0" x2="0" y2="1">
      <stop offset="0" stop-color="#3b80ab"/>
      <stop offset="0.55" stop-color="#5da5c2"/>
      <stop offset="1" stop-color="#8ccfd8"/>
    </linearGradient>
    <linearGradient id="face-top" x1="0" y1="1" x2="0.3" y2="0">
      <stop offset="0" stop-color="#e3f3ee"/>
      <stop offset="1" stop-color="#68b0e0"/>
    </linearGradient>
    <linearGradient id="reflection" x1="0" y1="0" x2="0" y2="1">
      <stop offset="0" stop-color="#9fd2e4" stop-opacity="0.6"/>
      <stop offset="1" stop-color="#ffffff" stop-opacity="0"/>
    </linearGradient>
    <linearGradient id="cast-shadow" x1="0" y1="0" x2="1" y2="1">
      <stop offset="0" stop-color="#b9c2c6" stop-opacity="0.55"/>
      <stop offset="1" stop-color="#ffffff" stop-opacity="0"/>
    </linearGradient>
  </defs>

  <!-- vertical axis -->
  <text class="axis-label" transform="translate(190 1212) rotate(-90)">Business Value</text>

  <!-- level guides -->
  <g class="level-guides">
    <line class="guide-line" x1="245" y1="568" x2="1375" y2="168"/>
    <line class="guide-line" x1="245" y1="690" x2="1375" y2="292"/>
    <line class="guide-line" x1="245" y1="813" x2="1375" y2="413"/>
    <line class="guide-line" x1="245" y1="938" x2="1375" y2="540"/>
    <line class="guide-line" x1="245" y1="1060" x2="1375" y2="660"/>
    <line class="guide-line" x1="245" y1="1183" x2="1375" y2="782"/>
  </g>

  <!-- ground shadows & reflections -->
  <g class="ground-effects">
    <polygon points="974,1072 1222,1040 1360,1060 1150,1170 974,1135" fill="url(#cast-shadow)"/>
    <polygon points="974,1072 1057,1100 1057,1240 974,1210" fill="url(#reflection)"/>
    <polygon points="703,1165 951,1138 1000,1150 830,1290 703,1230" fill="url(#cast-shadow)"/>
    <polygon points="703,1165 786,1195 786,1320 703,1290" fill="url(#reflection)"/>
    <polygon points="400,1275 680,1235 690,1260 590,1400 432,1330" fill="url(#cast-shadow)"/>
    <polygon points="432,1265 515,1292 515,1420 432,1395" fill="url(#reflection)"/>
  </g>

  <!-- level 1 -->
  <g class="stage stage-1">
    <polygon points="432,990 515,1018 515,1292 432,1265" fill="url(#face-left)"/>
    <polygon points="515,1018 680,962 680,1235 515,1292" fill="url(#face-right)"/>
    <polygon points="432,990 598,933 680,962 515,1018" fill="url(#face-top)"/>
    <text class="stage-name" text-anchor="middle" transform="translate(496 1145) rotate(-90) skewX(-12)">STEADY</text>
    <text class="step-label" text-anchor="middle" transform="translate(595 1062) rotate(-19)">Personas</text>
    <text class="step-label" text-anchor="middle" transform="translate(595 1138) rotate(-19)">Database</text>
    <text class="step-label" text-anchor="middle" transform="translate(595 1216) rotate(-19)">Systems</text>
    <text class="step-number" text-anchor="middle" x="556" y="975">1</text>
  </g>

  <!-- level 2 -->
  <g class="stage stage-2">
    <polygon points="703,652 786,680 786,1195 703,1165" fill="url(#face-left)"/>
    <polygon points="786,680 951,623 951,1138 786,1195" fill="url(#face-right)"/>
    <polygon points="703,652 870,594 951,623 786,680" fill="url(#face-top)"/>
    <text class="stage-name" text-anchor="middle" transform="translate(767 920) rotate(-90) skewX(-12)">HARVEST</text>
    <text class="step-label" text-anchor="middle" transform="translate(868 828) rotate(-19)">Messaging</text>
    <text class="step-label" text-anchor="middle" transform="translate(868 915) rotate(-19)">Leads</text>
    <text class="step-label" text-anchor="middle" transform="translate(868 998) rotate(-19)">Pipeline</text>
    <text class="step-number" text-anchor="middle" x="836" y="648">2</text>
  </g>

  <!-- level 3 -->
  <g class="stage stage-3">
    <polygon points="974,433 1057,462 1057,1100 974,1072" fill="url(#face-left)"/>
    <polygon points="1057,462 1222,405 1222,1040 1057,1100" fill="url(#face-right)"/>
    <polygon points="974,433 1140,375 1222,405 1057,462" fill="url(#face-top)"/>
    <text class="stage-name" text-anchor="middle" transform="translate(1034 802) rotate(-90) skewX(-12)">PATRONS</text>
    <text class="step-label" text-anchor="middle" transform="translate(1141 651) rotate(-19)">Sales</text>
    <text class="step-label" text-anchor="middle" transform="translate(1141 741) rotate(-19)">Nurture</text>
    <text class="step-label" text-anchor="middle" transform="translate(1141 829) rotate(-19)">Reference</text>
    <text class="step-number" text-anchor="middle" x="1107" y="420">3</text>
  </g>

  <!-- brand & title -->
  <text class="brand-name" text-anchor="middle" x="2008" y="812">SHP</text>
  <text class="programme-title" text-anchor="end" x="2093" y="940">Steady</text>
  <text class="programme-title" text-anchor="end" x="2093" y="990">Harvest of Patrons</text>

  <!-- cadence legend -->
  <g class="cadence-legend">
    <circle class="legend-dot" cx="1245" cy="1068" r="4.5"/>
    <line class="legend-line" x1="1245" y1="1068" x2="1318" y2="1068"/>
    <text class="legend-text" x="1353" y="1082">Monthly Scorecard</text>
    <text class="legend-text" text-anchor="middle" x="1738" y="1082">–</text>
    <text class="legend-text" text-anchor="end" x="2095" y="1082">Strategic Review</text>

    <circle class="legend-dot" cx="997" cy="1175" r="4.5"/>
    <line class="legend-line" x1="997" y1="1175" x2="1318" y2="1175"/>
    <text class="legend-text" x="1355" y="1191">Weekly Scorecard</text>
    <text class="legend-text" text-anchor="middle" x="1738" y="1191">–</text>
    <text class="legend-text" text-anchor="end" x="2097" y="1191">Tactical Execution</text>

    <circle class="legend-dot" cx="701" cy="1292" r="4.5"/>
    <line class="legend-line" x1="701" y1="1292" x2="1318" y2="1292"/>
    <text class="legend-text" x="1353" y="1305">Numbers that Matter</text>
    <text class="legend-text" text-anchor="middle" x="1738" y="1305">–</text>
    <text class="legend-text" text-anchor="end" x="2097" y="1305">Foundation Metrics</text>
  </g>
</svg>
</body>
</html>
```